Fjellmark Botanics - Black Face Mask Packaging Design

We require packaging design for a charcoal activated blackhead removal peel off face mask (please see attachment of competitors product).

1: We require a logo for our brand name: 'Fjellmark Botanics'

2: We require a 3d rendered image of the box with the tube

3: We require label templates for both the box and the tube

The logo design brief is as follows:

We are bringing out a range of natural beauty products. We require a logo that represents norwegian natural beauty & incorporates the Norwegian Flag.

The packaging design brief is as follows:

Please attachment: (FBGen). There is an image of a woman with a black face mask.

1:We require our packaging design to have a generic face with a face mask being pulled off/stretched (as shown in the above attachment).
However, the face mask should display a Norwegian flag. The part of the mask that is still fixed to the face should be in full pastel Norwegian flag colors. The part of the mask that has been peeled away should be faded to charcoal grey (whilst maintaining the Norwegian flag). The ratio should be around 50/50 of mask attached to mask being peeled.
The colors throughout should be soft.

2:The design should also incorporate a unisex logo.(Please see attachment: FBUnisex)

3: The design should display the wording: 'Charcoal Activated Face Mask'

4: The design should also display the tagline: 'restores your youthful glow'

5: The back of the tube should display the ingredients: Please see attached. The back should also say ISO901 & GMPC certified

Please note, the packaging design for the tube should just be black and white as the printing machine on the tube can only be white.

The box can be a variation of colors as there are no restrictions on the colors for printing onto cardboard

Target Market(s)

Beauty, Natural Beauty, Unisex

Industry/Entity Type

Product

Logo Text

Fjellmark Botanics

Requirements
Must have
• Please refer to project description
Nice to have

```html
<!DOCTYPE html>
<html lang="en">
<head>
<meta charset="utf-8">
<title>Fjellmark Botanics – Charcoal Activated Face Mask Tube Label</title>
<link href="https://fonts.googleapis.com/css2?family=Josefin+Sans:wght@400;600;700&display=swap" rel="stylesheet">
<style>
  :root {
    --page-bg: #e4e4e4;
    --label-white: #ffffff;
    --crimp-white: #f4f4f4;
    --navy-base: #1f4a8a;
    --text-navy: #1e2a6b;
    --photo-warm: #e9c9b4;
    --photo-red: #e3342f;
    --photo-blue: #2e3f8e;
  }
  * { box-sizing: border-box; margin: 0; padding: 0; }
  html, body { width: 1200px; height: 960px; overflow: hidden; }
  body {
    background: var(--page-bg);
    font-family: "Josefin Sans", sans-serif;
    display: flex;
    align-items: center;
    justify-content: center;
  }
  .tube-label {
    position: relative;
    width: 440px;
    height: 900px;
    background: var(--label-white);
    display: flex;
    flex-direction: column;
    align-items: center;
    box-shadow: 0 2px 10px rgba(0,0,0,0.08);
  }
  .crimp-seal {
    width: 100%;
    height: 56px;
    flex-shrink: 0;
    background: var(--crimp-white);
    border-bottom: 1px solid #e2e2e2;
  }
  .brand-name {
    margin-top: 96px;
    color: var(--text-navy);
    font-weight: 700;
    font-size: 36px;
    line-height: 1.15;
    letter-spacing: 0.5px;
    text-align: center;
  }
  .product-name {
    margin-top: 30px;
    color: var(--text-navy);
    text-transform: uppercase;
    font-weight: 400;
    font-size: 24px;
    letter-spacing: 0.5px;
    text-align: center;
    line-height: 1.3;
  }
  .tagline {
    margin-top: 12px;
    padding: 8px 4px 6px;
    border-top: 2px solid var(--text-navy);
    border-bottom: 2px solid var(--text-navy);
    color: var(--text-navy);
    font-size: 17px;
    font-weight: 600;
    width: 266px;
    text-align: center;
  }
  .hero-visual {
    margin-top: 40px;
    width: 286px;
    height: 270px;
    flex-shrink: 0;
    border-radius: 40px 40px 60px 60px;
    background:
      radial-gradient(ellipse at 70% 45%, var(--photo-red) 0%, rgba(227,52,47,0.55) 35%, transparent 60%),
      radial-gradient(ellipse at 25% 55%, var(--photo-blue) 0%, rgba(46,63,142,0.5) 30%, transparent 55%),
      linear-gradient(180deg, #8a6a52 0%, var(--photo-warm) 30%, #f3e2d6 100%);
    opacity: 0.9;
  }
  .volume {
    margin-top: auto;
    margin-bottom: 14px;
    font-size: 21px;
    font-weight: 600;
    color: #222;
    letter-spacing: 0.5px;
  }
  .cap-band {
    width: 100%;
    height: 118px;
    flex-shrink: 0;
    background: var(--navy-base);
  }
</style>
</head>
<body>
  <main class="tube-label">
    <div class="crimp-seal"></div>

    <p class="brand-name">Fjellmark<br>Botanics</p>

    <h1 class="product-name">Charcoal Activated<br>Face Mask</h1>
    <p class="tagline">Restores your Youthful Glow</p>

    <div class="hero-visual" role="img" aria-label="Photo of a person peeling off a face mask printed with the Norwegian flag"></div>

    <p class="volume">250ml</p>
    <div class="cap-band"></div>
  </main>
</body>
</html>
```